Alpforma Banner

Hi boys and girls :)

We have a little project 4u.

We need a banner in 4 sizes :

Leaderboard: 728*90
Wide SkyScraper: 160*600
Medium Rectangle: 300*250
Ribbon (special format): 990*45

Message on banner :

Either our Logo + Immigration, Integration, Naturalization

Or our Logo + Incorporation, Domicile, Secretarial Services

And if space allows for it www.alpforma-example.com as well.

We are looking for a clean design, check our Website for inspiration concerning colors.

```html
<!DOCTYPE html>
<html lang="en">
<head>
<meta charset="utf-8">
<title>Alpforma Leaderboard Banner</title>
<link href="https://fonts.googleapis.com/css2?family=Roboto+Condensed:wght@400;700&display=swap" rel="stylesheet">
<style>
  :root {
    --white: #ffffff;
    --ink: #2a2a2a;
    --street-dark: #2b2b2b;
    --street-mid: #5a5a5a;
    --street-light: #8a8a8a;
    --silver-light: #e4e4e4;
    --silver-dark: #9a9a9a;
    --accent-red: #e0141c;
    --accent-red-dark: #a80c12;
  }
  html, body {
    margin: 0;
    padding: 0;
    overflow: hidden;
    background: var(--white);
  }
  .banner {
    position: relative;
    width: 1200px;
    height: 148px;
    overflow: hidden;
    font-family: "Roboto Condensed", "Arial Narrow", sans-serif;
    background: var(--white);
  }
  .street-scene {
    position: absolute;
    inset: 0;
    background: linear-gradient(90deg, var(--street-dark) 0%, var(--street-mid) 45%, var(--street-light) 75%, var(--street-mid) 100%);
  }
  .shapes {
    position: absolute;
    inset: 0;
  }
  .brand {
    position: absolute;
    left: 18px;
    top: 0;
    height: 148px;
    display: flex;
    align-items: center;
    gap: 10px;
  }
  .brand-mark {
    width: 22px;
    height: 22px;
    background: var(--ink);
  }
  .brand-name {
    font-size: 38px;
    font-weight: 400;
    color: var(--ink);
    letter-spacing: 1px;
  }
  .services {
    position: absolute;
    left: 321px;
    top: 12px;
    margin: 0;
    text-transform: uppercase;
    line-height: 1;
  }
  .services span { display: block; }
  .service-lead {
    font-size: 27px;
    color: var(--white);
    letter-spacing: 0.5px;
  }
  .service-focus {
    font-size: 48px;
    color: var(--accent-red);
    margin-top: 2px;
  }
  .service-tail {
    font-size: 42px;
    color: var(--white);
    margin-top: 4px;
    letter-spacing: 0.5px;
  }
  .cta {
    position: absolute;
    left: 864px;
    top: 41px;
    width: 280px;
    height: 59px;
    box-sizing: border-box;
    padding: 0 12px 0 22px;
    display: flex;
    align-items: center;
    justify-content: space-between;
    border-radius: 8px;
    background: linear-gradient(180deg, var(--accent-red) 0%, var(--accent-red-dark) 100%);
    color: var(--white);
    font-size: 22px;
    font-weight: 700;
    text-decoration: none;
    text-transform: uppercase;
    box-shadow: 0 2px 6px rgba(0,0,0,0.5);
  }
  .cta-icon {
    width: 38px;
    height: 38px;
  }
</style>
</head>
<body>
  <div class="banner">
    <div class="street-scene" role="img" aria-label="Greyscale photograph of an old town street with shopfronts and cobblestones"></div>

    <svg class="shapes" width="1200" height="148" viewBox="0 0 1200 148" aria-hidden="true">
      <defs>
        <linearGradient id="silverBand" x1="0" y1="0" x2="1" y2="0">
          <stop offset="0" stop-color="var(--silver-dark)"/>
          <stop offset="0.5" stop-color="var(--silver-light)"/>
          <stop offset="1" stop-color="var(--silver-dark)"/>
        </linearGradient>
      </defs>
      <polygon points="0,0 290,0 232,148 0,148" fill="var(--white)"/>
      <polygon points="290,0 348,0 290,148 232,148" fill="url(#silverBand)"/>
    </svg>

    <div class="brand">
      <span class="brand-mark"></span>
      <span class="brand-name">Alpforma</span>
    </div>

    <h1 class="services">
      <span class="service-lead">Immigration</span>
      <span class="service-focus">Integration,</span>
      <span class="service-tail">Naturalization</span>
    </h1>

    <a class="cta" href="#">
      Find out more
      <svg class="cta-icon" viewBox="0 0 38 38" aria-hidden="true">
        <circle cx="19" cy="19" r="17" fill="var(--white)"/>
        <polyline points="15,11 23,19 15,27" fill="none" stroke="var(--accent-red)" stroke-width="5" stroke-linecap="round" stroke-linejoin="round"/>
      </svg>
    </a>
  </div>
</body>
</html>
```